Most captivating card ever!

Life Coach - Professional Adventurer - Entrepreneur
I need the worlds most amazing business card for my personal brand. This business card will mostly be used to give to prospective clients for life coaching and business coaching.
Be creative, be adventurous. It needs to stand out. Make people say.. I need this guy!
My background is as an entrepreneur and professional adventurer undertaking extreme expeditions. I am now moving into life coaching.
No specific design ideas, so you have full creativity. Show me your best.
Industry/Entity Type
Life Coaching
Contact Information for Business Card
Dan Pellow
itsdanp.com.au
0468215903
Colors
Designer to choose colors to be used in the design.
Look and feel

```html
<!DOCTYPE html>
<html lang="en">
<head>
<meta charset="utf-8">
<title>Dan Pellow — Business Card</title>
<link href="https://fonts.googleapis.com/css2?family=Raleway:wght@300;400;700&family=Arimo:wght@400&display=swap" rel="stylesheet">
<style>
  :root {
    --bg: #2e2e2e;
    --card: #23262b;
    --card-edge: #1a1c20;
    --silver: #c9cacc;
    --silver-soft: #9a9ca0;
    --rule: #b8b9bb;
  }
  * { margin: 0; padding: 0; box-sizing: border-box; }
  html, body { width: 1200px; height: 716px; overflow: hidden; background: var(--bg); }
  .stage { position: relative; width: 1200px; height: 716px; }

  .card {
    position: absolute;
    width: 520px; height: 300px;
    top: 208px;
    background: linear-gradient(160deg, #282b30 0%, var(--card) 60%, #1f2226 100%);
    border-radius: 22px;
    box-shadow: 0 0 0 1px var(--card-edge), 0 18px 40px rgba(0,0,0,.45);
    color: var(--silver);
    font-family: "Raleway", sans-serif;
    overflow: hidden;
  }
  .card--front { left: 50px; }
  .card--back { left: 630px; }

  /* identity block */
  .identity { position: absolute; display: flex; align-items: center; gap: 10px; }
  .card--front .identity { left: 70px; top: 112px; }
  .mark-square { width: 46px; height: 46px; background: var(--silver); flex: none; }
  .name { font-size: 30px; letter-spacing: .5px; line-height: 1; white-space: nowrap; }
  .name .first { font-weight: 300; }
  .name .last { font-weight: 700; }
  .tagline { font-size: 10.5px; font-weight: 400; color: var(--silver-soft); margin-top: 4px; white-space: nowrap; }

  .card--back .identity { left: 32px; top: 34px; }
  .accent-bar { width: 10px; height: 46px; background: var(--silver); flex: none; }
  .card--back .name { font-size: 26px; }

  /* contact list */
  .contacts { position: absolute; left: 34px; top: 166px; list-style: none; font-family: "Arimo", sans-serif; }
  .contacts li { display: flex; align-items: center; gap: 10px; font-size: 15px; color: var(--silver); height: 22px; }
  .contacts svg { width: 14px; height: 14px; fill: var(--silver); flex: none; }

  .rule { position: absolute; left: 0; top: 0; width: 520px; height: 300px; pointer-events: none; }

  .handle { position: absolute; right: 46px; bottom: 30px; display: flex; align-items: center; gap: 10px; font-family: "Arimo", sans-serif; font-size: 15px; color: var(--silver); }
  .handle .social-square { width: 14px; height: 14px; background: var(--silver-soft); }

  .brand-square { position: absolute; right: 44px; top: 138px; width: 64px; height: 64px; background: var(--silver); opacity: .85; }
</style>
</head>
<body>
<main class="stage">

  <section class="card card--front" aria-label="Card front">
    <div class="identity">
      <div class="mark-square"></div>
      <div>
        <div class="name"><span class="first">DAN</span> <span class="last">PELLOW</span></div>
        <div class="tagline">Life Coach - Professional Adventurer - Entrepreneur</div>
      </div>
    </div>
  </section>

  <section class="card card--back" aria-label="Card back">
    <div class="identity">
      <div class="accent-bar"></div>
      <div>
        <div class="name"><span class="first">DAN</span> <span class="last">PELLOW</span></div>
        <div class="tagline">Life Coach - Professional Adventurer - Entrepreneur</div>
      </div>
    </div>

    <ul class="contacts">
      <li>
        <svg viewBox="0 0 16 16"><path d="M2 5c0-2 2-3 6-3s6 1 6 3v1h-3V5H5v1H2z"/><rect x="3" y="8" width="10" height="6" rx="1"/></svg>
        0468215903
      </li>
      <li>
        <svg viewBox="0 0 16 16"><path d="M1 3h14v10H1z M2 4l6 5 6-5" fill="none" stroke="#c9cacc" stroke-width="1.4"/></svg>
        dan@itsdanp.com.au
      </li>
      <li>
        <svg viewBox="0 0 16 16"><g fill="none" stroke="#c9cacc" stroke-width="1.2"><circle cx="8" cy="8" r="6.5"/><ellipse cx="8" cy="8" rx="3" ry="6.5"/><path d="M1.5 8h13"/></g></svg>
        itsdanp.com.au
      </li>
    </ul>

    <svg class="rule" viewBox="0 0 520 300" aria-hidden="true">
      <path d="M0 242 H368 L380 234" fill="none" stroke="#b8b9bb" stroke-width="2"/>
    </svg>

    <div class="brand-square"></div>

    <div class="handle">/Danpellow <span class="social-square"></span></div>
  </section>

</main>
</body>
</html>
```